Brightfold - Elevating shareholder relations with a seamless SaaS communication platform

We need a landing page / web page for a new company based in Stockholm called "Brightfold". Our platform helps private companies communicate & connect with their shareholders and provides a cost efficient way of raising funds. We would like to see designs that use the color blue.

```html
<!DOCTYPE html>
<html lang="en">
<head>
<meta charset="utf-8">
<title>Brightfold – Shareholder Relations Platform</title>
<link href="https://fonts.googleapis.com/css2?family=Roboto:wght@400;500;700&family=Montserrat:wght@400;500&display=swap" rel="stylesheet">
<style>
:root{
  --blue:#174a8c;
  --blue-dark:#0f3a70;
  --blue-deep:#0c2f5e;
  --ink:#111111;
  --text:#4a4a4a;
  --muted:#777;
  --line:#e3e6ea;
  --soft:#eef0f3;
  --tint:#e6f0f5;
  --footer:#141414;
  --white:#fff;
}
*{box-sizing:border-box;margin:0;padding:0}
html,body{width:1200px;height:4827px;overflow:hidden}
body{font-family:"Roboto",Arial,sans-serif;color:var(--text);background:var(--white);position:relative}
section,header,footer{position:absolute;left:0;width:1200px}
.abs{position:absolute}
a{color:inherit;text-decoration:none}

/* header */
.site-header{top:0;height:141px;background:var(--white)}
.topbar{position:absolute;right:0;top:0;width:845px;height:47px;background:var(--blue);clip-path:polygon(0 0,100% 0,100% 100%,70px 100%)}
.topbar-items{position:absolute;right:110px;top:0;height:47px;display:flex;align-items:center;color:var(--white);font-size:16px}
.topbar-items span{display:flex;align-items:center;gap:8px;padding:0 18px}
.topbar-items .sep{width:1px;height:28px;background:rgba(255,255,255,.55);padding:0}
.brand{position:absolute;left:116px;top:26px;display:flex;flex-direction:column;align-items:center;gap:10px}
.brand-mark{width:58px;height:58px;background:var(--blue)}
.brand-name{font-family:"Montserrat",sans-serif;font-weight:500;font-size:19px;letter-spacing:3px;color:var(--blue)}
.main-nav{position:absolute;left:446px;top:82px;display:flex;font-size:16px;font-weight:500;color:var(--ink)}
.main-nav a{margin-right:56px}
.btn-login{position:absolute;left:960px;top:71px;width:128px;height:45px;background:var(--blue);color:var(--white);font-weight:500;font-size:16px;display:flex;align-items:center;justify-content:center;gap:8px;border-radius:2px}

/* hero */
.hero{top:141px;height:648px;background:
  radial-gradient(ellipse 420px 260px at 620px 420px,#bcd3ea 0%,rgba(150,185,220,.6) 45%,rgba(0,0,0,0) 100%),
  linear-gradient(180deg,#1c3c66 0%,#2f5b8e 35%,#5b86b6 60%,#24497a 100%)}
.hero-panel{position:absolute;left:244px;top:197px;width:712px;height:230px;background:rgba(120,130,145,.45);text-align:center}
.hero-title{margin-top:14px;font-size:32px;line-height:43px;font-weight:500;color:var(--white);text-transform:uppercase}
.btn-hero{display:inline-flex;margin-top:20px;width:166px;height:53px;align-items:center;justify-content:center;background:var(--blue);color:var(--white);font-weight:500;font-size:16px}
.dots{position:absolute;top:597px;left:552px;display:flex;gap:16px}
.dots i{width:11px;height:11px;border-radius:50%;background:rgba(255,255,255,.55)}
.dots i.on{background:var(--white)}

/* welcome */
.welcome{top:789px;height:630px}
.welcome-backdrop{position:absolute;left:120px;top:77px;width:316px;height:470px;background:var(--tint)}
.welcome-photo{position:absolute;left:165px;top:124px;width:430px;height:430px;background:linear-gradient(180deg,#eeeae2 0%,#d8c48a 38%,#8d8a6e 62%,#e9e6df 100%)}
.welcome-copy{position:absolute;left:649px;top:160px;width:440px}
h2{font-size:32px;font-weight:700;color:var(--ink);text-transform:uppercase}
.para{font-size:14px;line-height:27.5px;color:var(--text);margin-top:14px}
.btn-solid{display:inline-flex;align-items:center;justify-content:center;background:var(--blue);color:var(--white);font-weight:500;font-size:16px;text-transform:uppercase}

/* cta band */
.cta-band{top:1419px;height:197px;background:var(--blue)}
.cta-text{position:absolute;left:118px;top:57px;font-size:28px;line-height:45px;font-weight:700;color:var(--white);text-transform:uppercase}
.btn-contact{position:absolute;left:893px;top:74px;width:168px;height:52px;background:var(--white);color:var(--blue);font-weight:500;font-size:16px;display:flex;align-items:center;justify-content:center}

/* services */
.services{top:1616px;height:943px}
.section-title{position:absolute;left:0;width:1200px;text-align:center;font-size:38px;font-weight:700;color:var(--ink);text-transform:uppercase}
.service-card{position:absolute;width:312px;height:341px;border:1px solid var(--line);border-radius:4px;text-align:center}
.service-icon{width:101px;height:101px;border-radius:50%;background:var(--soft);margin:34px auto 0;display:flex;align-items:center;justify-content:center}
.service-card h3{margin-top:28px;font-size:22px;font-weight:500;color:var(--ink)}
.service-card .rule{width:46px;height:3px;background:var(--blue);margin:15px auto 0}
.service-card p{margin:16px auto 0;width:270px;font-size:14px;line-height:27.5px;color:var(--text)}

/* about */
.about{top:2559px;height:533px;background:var(--blue)}
.about-copy{position:absolute;left:126px;top:80px;width:440px;color:var(--white)}
.about-copy h2{color:var(--white)}
.about-copy .para{color:#e6ecf5}
.btn-outline{display:inline-flex;margin-top:28px;width:170px;height:53px;border:2px solid var(--white);align-items:center;justify-content:center;color:var(--white);font-weight:500;font-size:16px;text-transform:uppercase}
.about-photo{position:absolute;left:600px;top:0;width:600px;height:533px;background:linear-gradient(180deg,#8fa6c0 0%,#6f8096 30%,#2f3442 58%,#d9d4ca 80%,#a9a49b 100%)}

/* blog */
.blog{top:3092px;height:819px}
.blog-grid{position:absolute;left:116px;top:161px;width:972px;height:564px}
.tile{position:absolute;width:324px;height:282px}
.post{padding-left:15px}
.tag{display:inline-block;background:var(--blue);color:var(--white);font-size:10px;padding:5px 14px;border-radius:12px}
.post h3{margin-top:14px;font-size:20px;line-height:27px;font-weight:700;color:var(--ink)}
.meta{margin-top:8px;font-size:13px;font-style:italic;color:var(--text);display:flex;gap:16px;align-items:center}
.excerpt{margin-top:8px;font-size:14px;line-height:27.5px;color:var(--text);width:300px}
.read{margin-top:6px;font-size:14px;font-weight:700;color:var(--blue);display:flex;align-items:center;gap:10px}
.read::after{content:"";width:36px;height:1px;background:var(--blue)}

/* contact */
.contact{top:3911px;height:552px;background:linear-gradient(180deg,#1b4f93,#123f7a)}
.contact h2{position:absolute;left:0;width:1200px;text-align:center;top:94px;color:var(--white);font-size:38px}
.field{position:absolute;background:var(--white);font-family:"Montserrat",sans-serif;font-size:13px;color:#666;padding:17px 18px}
.btn-send{position:absolute;left:486px;top:420px;width:228px;height:49px;border:2px solid var(--white);border-radius:25px;color:var(--white);font-weight:500;font-size:16px;display:flex;align-items:center;justify-content:center}

/* footer */
.site-footer{top:4463px;height:364px;background:var(--footer);color:var(--white)}
.foot-brand{position:absolute;left:123px;top:70px;width:200px;display:flex;flex-direction:column;align-items:center;gap:18px}
.foot-brand .brand-mark{width:88px;height:88px;background:var(--white)}
.foot-brand .brand-name{color:var(--white);font-size:22px;letter-spacing:4px}
.socials{display:flex;gap:7px}
.socials i{width:30px;height:30px;border-radius:50%;background:var(--white)}
.foot-col{position:absolute;top:76px;font-size:13px}
.foot-col h4{font-size:15px;font-weight:700;margin-bottom:26px}
.foot-col li{list-style:none;line-height:28px}
.contact-row{display:flex;gap:14px;align-items:flex-start;line-height:22px;margin-bottom:22px}
.contact-row .ico{width:28px;height:28px;border-radius:50%;background:var(--blue);flex:none;display:flex;align-items:center;justify-content:center}
.subscribe{position:absolute;left:823px;top:187px;width:265px;height:50px;background:var(--white);border-radius:25px;color:#777;font-size:13px;display:flex;align-items:center;padding-left:18px;gap:8px}
.subscribe .go{position:absolute;right:2px;top:2px;width:46px;height:46px;border-radius:50%;background:var(--blue);display:flex;align-items:center;justify-content:center}
.foot-rule{position:absolute;left:110px;top:305px;width:980px;height:1px;background:#3a3a3a}
.copyright{position:absolute;left:0;top:327px;width:1200px;text-align:center;font-size:13px}
</style>
</head>
<body>

<header class="site-header">
  <div class="topbar"></div>
  <div class="topbar-items">
    <span>
      <svg width="15" height="15" viewBox="0 0 24 24" fill="#fff"><path d="M6.6 10.8a15 15 0 0 0 6.6 6.6l2.2-2.2a1 1 0 0 1 1-.25 11.4 11.4 0 0 0 3.6.57 1 1 0 0 1 1 1V20a1 1 0 0 1-1 1A17 17 0 0 1 3 4a1 1 0 0 1 1-1h3.5a1 1 0 0 1 1 1c0 1.25.2 2.45.57 3.57a1 1 0 0 1-.25 1z"/></svg>
      +1 888-888-8888</span>
    <i class="sep"></i>
    <span>
      <svg width="16" height="16" viewBox="0 0 24 24" fill="#fff"><path d="M2 11 22 3l-7 19-3-8z"/></svg>
      info@Brightfold.com</span>
    <i class="sep"></i>
    <span>
      <svg width="26" height="26" viewBox="0 0 26 26"><circle cx="13" cy="13" r="12" fill="#e9edf3"/></svg>
      EN
      <svg width="10" height="10" viewBox="0 0 10 10"><path d="M1 3l4 4 4-4" stroke="#fff" stroke-width="1.5" fill="none"/></svg>
    </span>
  </div>
  <a class="brand" href="#"><span class="brand-mark"></span><span class="brand-name">BRIGHTFOLD</span></a>
  <nav class="main-nav">
    <a href="#">HOME</a><a href="#">ABOUT</a><a href="#">SERVICES</a><a href="#">BLOG</a><a href="#">CONTACT</a>
  </nav>
  <a class="btn-login" href="#">LOGIN
    <svg width="12" height="14" viewBox="0 0 12 14" fill="#fff"><rect x="1" y="6" width="10" height="8" rx="1"/><path d="M3 6V4a3 3 0 0 1 6 0v2" stroke="#fff" stroke-width="1.6" fill="none"/></svg>
  </a>
</header>

<section class="hero" role="img" aria-label="Upward view of glass office towers against a blue sky">
  <svg class="abs" style="left:68px;top:292px" width="22" height="40" viewBox="0 0 22 40"><path d="M20 2 3 20l17 18" stroke="#fff" stroke-width="2" fill="none"/></svg>
  <svg class="abs" style="right:68px;top:292px" width="22" height="40" viewBox="0 0 22 40"><path d="M2 2l17 18L2 38" stroke="#fff" stroke-width="2" fill="none"/></svg>
  <div class="hero-panel">
    <h1 class="hero-title">Elevating shareholder relations<br>with a seamless SaaS communication<br>platform</h1>
    <a class="btn-hero" href="#">GET STARTED</a>
  </div>
  <div class="dots"><i></i><i class="on"></i><i></i><i></i></div>
</section>

<section class="welcome">
  <div class="welcome-backdrop" role="img" aria-label="Decorative accent framing the team photo"></div>
  <div class="welcome-photo" role="img" aria-label="Team of colleagues gathered around a table reviewing documents"></div>
  <div class="welcome-copy">
    <h2>Welcome to Brightfold</h2>
    <p class="para">Lorem ipsum dolor sit amet, consectedipiscing elit, sed do eiusmod tempor incididunt ut labore magna aliqua. Quis ipsum suspendisse ultrices gravida. Risus commodo viverra maecenas accumsan lacus vel facilisis. Lorem ipsum dolor sit amet, consectedipiscing elit, sed do eiusmod tempor incididunt</p>
    <p class="para">Lorem ipsum dolor sit amet, consectedipiscing elit, sed do eiusmod tempor incididunt ut labore magna aliqua. Quis ipsum suspendisse ultrices gravida. Risus commodo</p>
    <a class="btn-solid" href="#" style="margin-top:26px;width:170px;height:53px">Learn More</a>
  </div>
</section>

<section class="cta-band">
  <p class="cta-text">The standard Lorem Ipsum passage,<br>used since the 1500s</p>
  <a class="btn-contact" href="#">CONTACT US</a>
</section>

<section class="services">
  <h2 class="section-title" style="top:78px">Our Services</h2>

  <div class="service-card" style="left:116px;top:156px">
    <div class="service-icon"><svg width="48" height="48" viewBox="0 0 48 48" fill="none" stroke="#3b4f6b" stroke-width="1.6"><rect x="6" y="8" width="32" height="26" rx="2"/><path d="M6 14h32M11 20h14M11 25h10"/><circle cx="35" cy="34" r="7"/><path d="M32 34l2 2 4-4"/></svg></div>
    <h3>Finibus Bonorum</h3><div class="rule"></div>
    <p>Lorem ipsum dolor sit amet, consectetur adipiscing elit, semod tempor incididunt ut labore et dolore magna aliqua.</p>
  </div>
  <div class="service-card" style="left:446px;top:156px">
    <div class="service-icon"><svg width="48" height="48" viewBox="0 0 48 48" fill="none" stroke="#3b4f6b" stroke-width="1.6"><path d="M24 6l14 5v11c0 9-6 15-14 19-8-4-14-10-14-19V11z"/><circle cx="24" cy="21" r="5"/><path d="M17 32c2-4 12-4 14 0"/></svg></div>
    <h3>Finibus Bonorum</h3><div class="rule"></div>
    <p>Lorem ipsum dolor sit amet, consectetur adipiscing elit, semod tempor incididunt ut labore et dolore magna aliqua.</p>
  </div>
  <div class="service-card" style="left:776px;top:156px">
    <div class="service-icon"><svg width="48" height="48" viewBox="0 0 48 48" fill="none" stroke="#3b4f6b" stroke-width="1.6"><rect x="6" y="5" width="10" height="10" rx="1"/><rect x="32" y="5" width="10" height="10" rx="1"/><rect x="6" y="33" width="10" height="8" rx="1"/><rect x="32" y="33" width="10" height="8" rx="1"/><path d="M14 24c4-6 16-6 20 0-4 6-16 6-20 0z"/><circle cx="24" cy="24" r="3"/></svg></div>
    <h3>Finibus Bonorum</h3><div class="rule"></div>
    <p>Lorem ipsum dolor sit amet, consectetur adipiscing elit, semod tempor incididunt ut labore et dolore magna aliqua.</p>
  </div>
  <div class="service-card" style="left:116px;top:518px">
    <div class="service-icon"><svg width="48" height="48" viewBox="0 0 48 48" fill="none" stroke="#3b4f6b" stroke-width="1.6"><rect x="6" y="16" width="26" height="22" rx="2"/><path d="M11 23h14M11 29h10"/><circle cx="34" cy="14" r="7"/><path d="M34 10v4l3 2"/><path d="M32 30h10l-3-3M42 30l-3 3"/></svg></div>
    <h3>Finibus Bonorum</h3><div class="rule"></div>
    <p>Lorem ipsum dolor sit amet, consectetur adipiscing elit, semod tempor incididunt ut labore et dolore magna aliqua.</p>
  </div>
  <div class="service-card" style="left:446px;top:518px">
    <div class="service-icon"><svg width="48" height="48" viewBox="0 0 48 48" fill="none" stroke="#3b4f6b" stroke-width="1.6"><rect x="10" y="6" width="28" height="36" rx="2"/><circle cx="19" cy="16" r="4"/><path d="M28 14h6M28 19h6"/><rect x="18" y="28" width="12" height="10" rx="1"/><path d="M21 28v-3a3 3 0 0 1 6 0v3"/></svg></div>
    <h3>Finibus Bonorum</h3><div class="rule"></div>
    <p>Lorem ipsum dolor sit amet, consectetur adipiscing elit, semod tempor incididunt ut labore et dolore magna aliqua.</p>
  </div>
  <div class="service-card" style="left:776px;top:518px">
    <div class="service-icon"><svg width="48" height="48" viewBox="0 0 48 48" fill="none" stroke="#3b4f6b" stroke-width="1.6"><path d="M6 12h12l4 4h20v22H6z"/><path d="M6 20h36"/><path d="M18 30c3-5 11-5 14 0-3 5-11 5-14 0z"/><circle cx="25" cy="30" r="2"/></svg></div>
    <h3>Finibus Bonorum</h3><div class="rule"></div>
    <p>Lorem ipsum dolor sit amet, consectetur adipiscing elit, semod tempor incididunt ut labore et dolore magna aliqua.</p>
  </div>
</section>

<section class="about">
  <div class="about-copy">
    <h2>About Us</h2>
    <p class="para">Lorem ipsum dolor sit amet, consectedipiscing elit, sed do eiusmod tempor incididunt ut labore magna aliqua. Quis ipsum suspendisse ultrices gravida. Risus commodo viverra maecenas accumsan lacus vel facilisis. Lorem ipsum dolor sit amet, consectedipiscing elit, sed do eiusmod tempor incididunt</p>
    <p class="para">Lorem ipsum dolor sit amet, consectedipiscing elit, sed do eiusmod tempor incididunt ut labore magna aliqua. Quis ipsum suspendisse ultrices gravida. Risus commodo</p>
    <a class="btn-outline" href="#">Learn More</a>
  </div>
  <div class="about-photo" role="img" aria-label="Business professionals in a meeting beside a window overlooking the city"></div>
</section>

<section class="blog">
  <h2 class="section-title" style="top:78px">Latest Blog</h2>
  <div class="blog-grid">
    <div class="tile" style="left:0;top:0;background:linear-gradient(160deg,#1f3e66 0%,#6f8fb3 35%,#dfe5ec 70%,#9fb2c7 100%)" role="img" aria-label="Hands reviewing financial charts on a tablet"></div>
    <article class="tile post" style="left:324px;top:0;padding-top:44px">
      <span class="tag">Finibus Bon</span>
      <h3>The standard Lorem&nbsp; passage,<br>used since the 1500s</h3>
      <div class="meta">February 21,2022 <span>&#128172;&#xFE0E; 0</span></div>
      <p class="excerpt">Lorem ipsum dolor sit amet, conetur adipiscing elit, sed do eiusmod tempor</p>
      <a class="read" href="#">Read More</a>
    </article>
    <div class="tile" style="left:648px;top:0;background:linear-gradient(200deg,#2b3440 0%,#6d7784 40%,#d9dde2 75%,#b8bec6 100%)" role="img" aria-label="Business people walking up modern outdoor stairs"></div>

    <article class="tile post" style="left:0;top:282px;padding-top:30px;padding-left:0">
      <span class="tag">Finibus Bon</span>
      <h3>The standard Lorem&nbsp; passage,<br>used since the 1500s</h3>
      <div class="meta">February 21,2022 <span>&#128172;&#xFE0E; 0</span></div>
      <p class="excerpt">Lorem ipsum dolor sit amet, conetur adipiscing elit, sed do eiusmod tempor</p>
      <a class="read" href="#">Read More</a>
    </article>
    <div class="tile" style="left:324px;top:282px;background:linear-gradient(180deg,#3d5f8c 0%,#6f87a8 35%,#b08a7a 60%,#2a2733 100%)" role="img" aria-label="Modern glass towers at dusk with light trails"></div>
    <article class="tile post" style="left:648px;top:282px;padding-top:30px;padding-left:25px">
      <span class="tag">Finibus Bon</span>
      <h3>The standard Lorem&nbsp; passage,<br>used since the 1500s</h3>
      <div class="meta">February 21,2022 <span>&#128172;&#xFE0E; 0</span></div>
      <p class="excerpt">Lorem ipsum dolor sit amet, conetur adipiscing elit, sed do eiusmod tempor</p>
      <a class="read" href="#">Read More</a>
    </article>
  </div>
</section>

<section class="contact">
  <h2>Get in Touch With Us</h2>
  <div class="field" style="left:274px;top:171px;width:319px;height:49px">Your Name</div>
  <div class="field" style="left:608px;top:171px;width:318px;height:49px">Email address</div>
  <div class="field" style="left:274px;top:233px;width:319px;height:49px">Contact number</div>
  <div class="field" style="left:608px;top:233px;width:318px;height:49px">subject</div>
  <div class="field" style="left:274px;top:295px;width:652px;height:112px">Message</div>
  <a class="btn-send" href="#">SEND MESSAGE</a>
</section>

<footer class="site-footer">
  <div class="foot-brand">
    <span class="brand-mark"></span>
    <span class="brand-name">BRIGHTFOLD</span>
    <div class="socials"><i></i><i></i><i></i><i></i></div>
  </div>
  <div class="foot-col" style="left:383px">
    <h4>QUICK LINKS</h4>
    <ul><li>Home</li><li>About</li><li>Services</li><li>Blog</li><li>Contact</li></ul>
  </div>
  <div class="foot-col" style="left:544px">
    <h4>CONTACT US</h4>
    <div class="contact-row"><span class="ico"><svg width="12" height="14" viewBox="0 0 12 16" fill="#fff"><path d="M6 0a6 6 0 0 0-6 6c0 4.5 6 10 6 10s6-5.5 6-10a6 6 0 0 0-6-6zm0 8.5A2.5 2.5 0 1 1 6 3.5a2.5 2.5 0 0 1 0 5z"/></svg></span><span>123 Avenue name, City<br>name 10150, United States</span></div>
    <div class="contact-row"><span class="ico"><svg width="12" height="12" viewBox="0 0 24 24" fill="#fff"><path d="M6.6 10.8a15 15 0 0 0 6.6 6.6l2.2-2.2a1 1 0 0 1 1-.25 11.4 11.4 0 0 0 3.6.57 1 1 0 0 1 1 1V20a1 1 0 0 1-1 1A17 17 0 0 1 3 4a1 1 0 0 1 1-1h3.5a1 1 0 0 1 1 1c0 1.25.2 2.45.57 3.57a1 1 0 0 1-.25 1z"/></svg></span><span>+1 888 888 8888</span></div>
    <div class="contact-row"><span class="ico"><svg width="13" height="10" viewBox="0 0 14 10" fill="none" stroke="#fff" stroke-width="1.4"><rect x="1" y="1" width="12" height="8"/><path d="M1 1l6 5 6-5"/></svg></span><span>info@Brightfold.com</span></div>
  </div>
  <div class="foot-col" style="left:823px">
    <h4>SUBSCRIBE TO OUR BLOG</h4>
    <p style="line-height:28px">Sign up today to get resources on how<br>to attract and retain more customers!</p>
  </div>
  <div class="subscribe">
    <svg width="13" height="10" viewBox="0 0 14 10" fill="none" stroke="#777" stroke-width="1.3"><rect x="1" y="1" width="12" height="8"/><path d="M1 1l6 5 6-5"/></svg>
    Email Address
    <span class="go"><svg width="18" height="18" viewBox="0 0 24 24" fill="#fff"><path d="M2 11 22 3l-7 19-3-8z"/></svg></span>
  </div>
  <div class="foot-rule"></div>
  <p class="copyright">Copyright © 2022. Brightfold.All Rights Reserved&nbsp; |&nbsp; Privacy Policy</p>
</footer>

</body>
</html>
```